Church Offering Envelope for receive weekly offerings

I need the front of an 6 3/4 envelope designed to be a church offering envelope. Our color palette is CMYK, 1a56b7, e8da7e, 19a3a3, 40c7f1, e7282d.
I need all of the text information carried forward from our old envelope (see attached) but the new style needs to be modern and flat. (Don't want another dove and clouds theme) I need a 1/4 border on all four sides as envelopes cannot be printed full bleed.
Logo is attached
Target Market(s)
Church
Industry/Entity Type
Church
Font styles to use
Sans Serif
Requirements
Must have
- must adhere to the color palette is CMYK, 1a56b7, e8da7e, 19a3a3, 40c7f1, e7282d.
- I need all of the text information carried forward from our old envelope (see attached)

```html
<!DOCTYPE html>
<html lang="en">
<head>
<meta charset="utf-8">
<title>Grace Harbor Ministries – Offering Envelope</title>
<link rel="stylesheet" href="https://fonts.googleapis.com/css2?family=Roboto+Condensed:wght@400&family=Roboto+Slab:wght@400&family=Yesteryear&display=swap">
<style>
  :root {
    --stage: #ebe8e4;
    --paper: #ffffff;
    --paper-shade: #f1f2f3;
    --red: #e7282d;
    --teal: #21a5a6;
    --maroon: #8a1c32;
    --label: #4a4a4a;
    --rule: #b9b9b9;
    --quote: #19a3a3;
    --faint: #e3eff1;
  }
  * { margin: 0; padding: 0; box-sizing: border-box; }
  html, body { width: 1200px; height: 1035px; overflow: hidden; }
  body { background: var(--stage); position: relative; font-family: "Roboto Condensed", sans-serif; }

  .envelope {
    position: absolute;
    width: 974px;
    height: 459px;
    background: var(--paper);
    box-shadow: 0 2px 6px rgba(0,0,0,.18);
    overflow: hidden;
  }
  .envelope--back-red  { left: 190px; top: 34px; }
  .envelope--back-teal { left: 144px; top: 313px; background: linear-gradient(135deg, var(--paper) 40%, var(--paper-shade)); }
  .envelope--front     { left: 63px;  top: 543px; }

  .flap { position: absolute; left: 0; top: 0; width: 974px; height: 155px; display: block; }
  .flap-name {
    position: absolute; left: 0; width: 100%; text-align: center;
    font-family: "Roboto Slab", serif; font-size: 25px; color: #fff; letter-spacing: .5px;
  }
  .envelope--back-red  .flap-name { top: 60px; }
  .envelope--back-teal .flap-name { top: 68px; }

  .ministry-name {
    position: absolute; left: 44px; top: 84px;
    font-family: "Roboto Slab", serif; font-size: 38px; color: var(--maroon); letter-spacing: 1px;
    display: flex; align-items: center; gap: 12px;
  }
  .ministry-name .dot { width: 14px; height: 14px; border-radius: 50%; background: var(--maroon); }

  .decor-circle {
    position: absolute; left: 610px; top: 40px; width: 300px; height: 300px;
    border-radius: 50%; border: 22px solid var(--faint);
  }

  .verse {
    position: absolute; right: 60px; top: 230px; text-align: right;
    font-family: "Yesteryear", cursive; font-size: 17px; line-height: 24px; color: var(--quote);
  }
  .verse .ref { display: block; font-family: "Roboto Condensed", sans-serif; font-style: italic; font-size: 15px; color: var(--red); text-align: center; padding-left: 120px; }

  .field { position: absolute; font-size: 20px; color: var(--label); display: flex; align-items: flex-end; }
  .field .line { border-bottom: 1px solid var(--rule); height: 1px; margin-bottom: 4px; }
  .field--name     { left: 44px;  top: 308px; }
  .field--name .line { width: 596px; margin-left: 32px; }
  .field--tithe    { left: 44px;  top: 350px; }
  .field--tithe .line { width: 197px; margin-left: 6px; }
  .field--radio    { left: 403px; top: 350px; }
  .field--radio .line { width: 162px; margin-left: 34px; }

  .band-rule { position: absolute; left: 0; top: 403px; width: 100%; height: 3px; background: var(--red); }
  .band {
    position: absolute; left: 0; top: 409px; width: 100%; height: 56px; background: var(--teal);
    display: flex; align-items: center; padding-left: 48px; gap: 26px;
    font-family: "Roboto Slab", serif; font-size: 18px; color: #fff;
  }
  .band .dot { width: 22px; height: 22px; border-radius: 50%; border: 2px solid #fff; }
</style>
</head>
<body>

  <section class="envelope envelope--back-red" aria-label="Envelope back, red flap">
    <svg class="flap" viewBox="0 0 974 155" aria-hidden="true">
      <path d="M0 0 H974 C966 32 952 50 900 62 L520 148 Q487 155 454 148 L74 62 C22 50 8 32 0 0 Z" fill="var(--red)"/>
    </svg>
    <div class="flap-name">Grace Harbor Ministries</div>
  </section>

  <section class="envelope envelope--back-teal" aria-label="Envelope back, teal flap">
    <svg class="flap" viewBox="0 0 974 155" aria-hidden="true">
      <path d="M0 0 H974 C966 32 952 50 900 62 L520 148 Q487 155 454 148 L74 62 C22 50 8 32 0 0 Z" fill="var(--teal)"/>
    </svg>
    <div class="flap-name">Grace Harbor Ministries</div>
  </section>

  <section class="envelope envelope--front" aria-label="Offering envelope front">
    <div class="decor-circle" aria-hidden="true"></div>
    <div class="ministry-name"><span class="dot"></span>Grace Harbor Ministries</div>

    <p class="verse">“Honour the LORD with the Substance,<br>and win the firt fruits of all thine increase:”
      <span class="ref">Prov3:9</span></p>

    <div class="field field--name">Name<span class="line"></span></div>
    <div class="field field--tithe">Tithe/Offering<span class="line"></span></div>
    <div class="field field--radio">Radio/Webcast<span class="line"></span></div>

    <div class="band-rule"></div>
    <div class="band"><span class="dot"></span>Grace Harbor Ministries does not receive restricted funds in amounts less than $ 10,000</div>
  </section>

</body>
</html>
```